Hochwertiges Etiketten-Design für edle Destillate
Zielgruppe
Wir sind ein Familiengeführter Brennereibetrieb wo wir edle Destillate (Obstbrände und Liköre) herstellen.
Aufgabenstellung
Wir suchen ein hochwertiges Etikett welches eine sofortige Wiedererkennung hat. Unser jetziges Etikett soll als Vorlage gelten, jedoch einiges aufgewertet werden. Unser Logo und und die Farbe Rot soll auf jeden Fall darin vorkommen.
Dies sind unsere verwendeten Flaschen
https://www.vandoro.com/kelm-flasche-500ml-weissglas-mdg.-gpi-28-karton-50stk.html?cPath=5_6
https://www.vandoro.com/kelm-flasche-200ml-weissglas-mdg.-gpi-28-karton-45stk.html?cPath=5_6
https://www.vandoro.com/urma-500-ml-weissglas-mdg.-gpi-28-karton-46stk.html?cPath=5_6
https://www.vandoro.com/urma-200ml-weissglas-mdg.-gpi-28-karton-90stk.html?cPath=5_6
das Design soll skalierbar und auf andere Größen anwendbar sein
Folgende Angaben müssen auf dem Etikett sein (austauschbar):
-Sorte: z.B. Williams
-Produkt: zB. Birnenbrand
-Losnummer: z.B. K3F57382
-Inhalt: z.B. 500ml
-Alkoholgehalt: 40% vol
-Adresse

```html
<!DOCTYPE html>
<html lang="de">
<head>
<meta charset="utf-8">
<title>Hallbrunner Edelbrände – Etiketten</title>
<link rel="stylesheet" href="https://fonts.googleapis.com/css2?family=Oswald:wght@400;500;600&family=Libre+Caslon+Text:wght@400&family=Roboto+Condensed:wght@400;700&family=Mrs+Saint+Delafield&display=swap">
<style>
  :root {
    --stage: #e4e4e4;
    --page: #ffffff;
    --slate-light: #3a3f45;
    --slate-mid: #1b1e22;
    --slate-dark: #050506;
    --red: #e30613;
    --red-deep: #b3121c;
    --white: #ffffff;
    --grey-text: #d9d9d9;
  }
  * { box-sizing: border-box; margin: 0; padding: 0; }
  html, body { width: 1200px; height: 2201px; overflow: hidden; background: var(--page); }
  .sheet { position: relative; width: 1200px; height: 2201px; }
  .stage { position: absolute; left: 0; top: 0; width: 1200px; height: 1107px; background: var(--stage); }

  .label {
    position: absolute;
    container-type: size;
    color: var(--white);
    background: radial-gradient(ellipse at 45% 40%, var(--slate-light) 0%, var(--slate-mid) 45%, var(--slate-dark) 100%);
    overflow: hidden;
  }
  .label--narrow { width: 154px; height: 335px; }
  .label--wide { width: 280px; height: 335px; }
  .stage .label--narrow { width: 285px; height: 620px; }
  .stage .label--wide { width: 517px; height: 620px; }

  .brand-tab {
    position: absolute; left: 50%; top: 0; transform: translateX(-50%);
    width: 17cqh; height: 9.5cqh; background: var(--red);
    display: flex; align-items: flex-end; justify-content: center; padding-bottom: 1.2cqh;
    font-family: "Libre Caslon Text", serif; font-size: 1.9cqh; letter-spacing: 0.03em; white-space: nowrap;
  }
  .house-line {
    position: absolute; left: 0; right: 0; top: 12.3cqh; text-align: center;
    font-family: "Libre Caslon Text", serif; font-size: 2.6cqh; letter-spacing: 0.12em; color: var(--grey-text);
  }
  .variety {
    position: absolute; left: 4%; right: 4%; top: 19cqh; height: 40cqh;
    display: flex; flex-direction: column; align-items: center; justify-content: center; gap: 1.5cqh;
  }
  .origin {
    font-family: "Oswald", sans-serif; font-weight: 500; font-size: min(3.4cqh, 6.2cqw); letter-spacing: 0.22em;
    text-align: center; line-height: 1.4; padding-left: 0.22em; white-space: nowrap;
  }
  .script-name {
    font-family: "Mrs Saint Delafield", cursive; font-size: min(17cqh, 29cqw); line-height: 1.15;
    white-space: nowrap; max-width: 100%; text-align: center;
  }
  .product {
    position: absolute; left: 0; right: 0; top: 60cqh;
    display: flex; align-items: center; justify-content: center; gap: 5cqh;
  }
  .product-text {
    font-family: "Oswald", sans-serif; font-weight: 600; font-size: 3.6cqh; letter-spacing: 0.55em;
    text-align: center; line-height: 1.35; padding-left: 0.55em;
  }
  .ornament { width: 7cqh; height: 1.2cqh; background: var(--red-deep); opacity: 0.75; }

  .maker { display: flex; align-items: center; gap: 0.8cqh; font-family: "Roboto Condensed", sans-serif; font-weight: 700; font-size: 2cqh; }
  .maker-dot { width: 3.4cqh; height: 3.4cqh; border-radius: 50%; background: var(--red); flex: none; }

  .address { font-family: "Roboto Condensed", sans-serif; font-size: 1.45cqh; line-height: 1.55; color: var(--grey-text); white-space: nowrap; }
  .address .web { font-weight: 700; color: var(--white); }
  .address .web span { color: var(--red); }
  .address .lot { margin-top: 0.9cqh; }

  .label--narrow .maker { position: absolute; left: 4%; top: 79cqh; flex-direction: column; gap: 0.5cqh; }
  .label--narrow .address { position: absolute; left: 40%; right: 2%; top: 77cqh; font-size: 1.3cqh; }
  .label--wide .maker { position: absolute; left: 0; right: 0; top: 75cqh; justify-content: center; }
  .label--wide .address { position: absolute; left: 0; right: 0; top: 84.5cqh; text-align: center; }

  .specs {
    position: absolute; left: 6%; right: 6%; bottom: 2.5cqh;
    display: flex; justify-content: space-between;
    font-family: "Oswald", sans-serif; font-weight: 500; font-size: 4cqh; letter-spacing: 0.04em; white-space: nowrap;
  }
</style>
</head>
<body>
<main class="sheet">
  <section class="stage">
    <article class="label label--narrow" style="left:149px; top:240px;">
      <div class="brand-tab">HALLBRUNNER</div>
      <div class="house-line">EDELBRÄNDE</div>
      <div class="variety"><div class="origin">TÜRKEN</div><div class="script-name">Kirsche</div></div>
      <div class="product"><span class="ornament" role="img" aria-label="Rotes Zierornament"></span><span class="product-text">BRAND</span><span class="ornament" role="img" aria-label="Rotes Zierornament"></span></div>
      <div class="maker"><span class="maker-dot"></span>Hallbrunner</div>
      <div class="address"><p>Edeldestillerie Hallbrunner</p><p>Lindenhofweg 4 · 79110 Sonnbach</p><p class="web">www.<span>brennerei-hallbrunner</span>.de</p><p class="lot">Losnummer K3F57382</p></div>
      <div class="specs"><span>40 % VOL.</span><span>500 ML ℮</span></div>
    </article>
    <article class="label label--wide" style="left:534px; top:240px;">
      <div class="brand-tab">HALLBRUNNER</div>
      <div class="house-line">EDELBRÄNDE</div>
      <div class="variety"><div class="script-name">Williams</div></div>
      <div class="product"><span class="ornament" role="img" aria-label="Rotes Zierornament"></span><span class="product-text">BIRNEN<br>BRAND</span><span class="ornament" role="img" aria-label="Rotes Zierornament"></span></div>
      <div class="maker"><span class="maker-dot"></span>Hallbrunner</div>
      <div class="address"><p>Edeldestillerie Hallbrunner · Lindenhofweg 4 · 79110 Sonnbach</p><p class="web">www.<span>brennerei-hallbrunner</span>.de</p><p>Losnummer K3F57382</p></div>
      <div class="specs"><span>40 % VOL.</span><span>500 ML ℮</span></div>
    </article>
  </section>

  <article class="label label--narrow" style="left:81px; top:1287px;">
    <div class="brand-tab">HALLBRUNNER</div>
    <div class="house-line">EDELBRÄNDE</div>
    <div class="variety"><div class="script-name">Williams</div></div>
    <div class="product"><span class="ornament" role="img" aria-label="Rotes Zierornament"></span><span class="product-text">BIRNEN<br>BRAND</span><span class="ornament" role="img" aria-label="Rotes Zierornament"></span></div>
    <div class="maker"><span class="maker-dot"></span>Hallbrunner</div>
    <div class="address"><p>Edeldestillerie Hallbrunner</p><p>Lindenhofweg 4 · 79110 Sonnbach</p><p class="web">www.<span>brennerei-hallbrunner</span>.de</p><p class="lot">Losnummer K3F57382</p></div>
    <div class="specs"><span>40 % VOL.</span><span>500 ML ℮</span></div>
  </article>
  <article class="label label--wide" style="left:291px; top:1287px;">
    <div class="brand-tab">HALLBRUNNER</div>
    <div class="house-line">EDELBRÄNDE</div>
    <div class="variety"><div class="script-name">Williams</div></div>
    <div class="product"><span class="ornament" role="img" aria-label="Rotes Zierornament"></span><span class="product-text">BIRNEN<br>BRAND</span><span class="ornament" role="img" aria-label="Rotes Zierornament"></span></div>
    <div class="maker"><span class="maker-dot"></span>Hallbrunner</div>
    <div class="address"><p>Edeldestillerie Hallbrunner · Lindenhofweg 4 · 79110 Sonnbach</p><p class="web">www.<span>brennerei-hallbrunner</span>.de</p><p>Losnummer K3F57382</p></div>
    <div class="specs"><span>40 % VOL.</span><span>500 ML ℮</span></div>
  </article>
  <article class="label label--narrow" style="left:652px; top:1289px;">
    <div class="brand-tab">HALLBRUNNER</div>
    <div class="house-line">EDELBRÄNDE</div>
    <div class="variety"><div class="origin">OBER<br>ÖSTERREICHISCHE</div><div class="script-name">Weinbirne</div></div>
    <div class="product"><span class="ornament" role="img" aria-label="Rotes Zierornament"></span><span class="product-text">BRAND</span><span class="ornament" role="img" aria-label="Rotes Zierornament"></span></div>
    <div class="maker"><span class="maker-dot"></span>Hallbrunner</div>
    <div class="address"><p>Edeldestillerie Hallbrunner</p><p>Lindenhofweg 4 · 79110 Sonnbach</p><p class="web">www.<span>brennerei-hallbrunner</span>.de</p><p class="lot">Losnummer K3F57382</p></div>
    <div class="specs"><span>40 % VOL.</span><span>500 ML ℮</span></div>
  </article>
  <article class="label label--wide" style="left:861px; top:1289px;">
    <div class="brand-tab">HALLBRUNNER</div>
    <div class="house-line">EDELBRÄNDE</div>
    <div class="variety"><div class="origin">OBERÖSTERREICHISCHE</div><div class="script-name">Weinbirne</div></div>
    <div class="product"><span class="ornament" role="img" aria-label="Rotes Zierornament"></span><span class="product-text">BRAND</span><span class="ornament" role="img" aria-label="Rotes Zierornament"></span></div>
    <div class="maker"><span class="maker-dot"></span>Hallbrunner</div>
    <div class="address"><p>Edeldestillerie Hallbrunner · Lindenhofweg 4 · 79110 Sonnbach</p><p class="web">www.<span>brennerei-hallbrunner</span>.de</p><p>Losnummer K3F57382</p></div>
    <div class="specs"><span>40 % VOL.</span><span>500 ML ℮</span></div>
  </article>

  <article class="label label--narrow" style="left:81px; top:1653px;">
    <div class="brand-tab">HALLBRUNNER</div>
    <div class="house-line">EDELBRÄNDE</div>
    <div class="variety"><div class="origin">SCHWARZ<br>WÄLDER</div><div class="script-name">Kirsch</div></div>
    <div class="product"><span class="ornament" role="img" aria-label="Rotes Zierornament"></span><span class="product-text">BRAND</span><span class="ornament" role="img" aria-label="Rotes Zierornament"></span></div>
    <div class="maker"><span class="maker-dot"></span>Hallbrunner</div>
    <div class="address"><p>Edeldestillerie Hallbrunner</p><p>Lindenhofweg 4 · 79110 Sonnbach</p><p class="web">www.<span>brennerei-hallbrunner</span>.de</p><p class="lot">Losnummer K3F57382</p></div>
    <div class="specs"><span>40 % VOL.</span><span>500 ML ℮</span></div>
  </article>
  <article class="label label--wide" style="left:291px; top:1653px;">
    <div class="brand-tab">HALLBRUNNER</div>
    <div class="house-line">EDELBRÄNDE</div>
    <div class="variety"><div class="origin">SCHWARZWÄLDER</div><div class="script-name">Kirsch</div></div>
    <div class="product"><span class="ornament" role="img" aria-label="Rotes Zierornament"></span><span class="product-text">BRAND</span><span class="ornament" role="img" aria-label="Rotes Zierornament"></span></div>
    <div class="maker"><span class="maker-dot"></span>Hallbrunner</div>
    <div class="address"><p>Edeldestillerie Hallbrunner · Lindenhofweg 4 · 79110 Sonnbach</p><p class="web">www.<span>brennerei-hallbrunner</span>.de</p><p>Losnummer K3F57382</p></div>
    <div class="specs"><span>40 % VOL.</span><span>500 ML ℮</span></div>
  </article>
  <article class="label label--narrow" style="left:652px; top:1655px;">
    <div class="brand-tab">HALLBRUNNER</div>
    <div class="house-line">EDELBRÄNDE</div>
    <div class="variety"><div class="origin">TÜRKEN</div><div class="script-name">Kirsche</div></div>
    <div class="product"><span class="ornament" role="img" aria-label="Rotes Zierornament"></span><span class="product-text">BRAND</span><span class="ornament" role="img" aria-label="Rotes Zierornament"></span></div>
    <div class="maker"><span class="maker-dot"></span>Hallbrunner</div>
    <div class="address"><p>Edeldestillerie Hallbrunner</p><p>Lindenhofweg 4 · 79110 Sonnbach</p><p class="web">www.<span>brennerei-hallbrunner</span>.de</p><p class="lot">Losnummer K3F57382</p></div>
    <div class="specs"><span>40 % VOL.</span><span>500 ML ℮</span></div>
  </article>
  <article class="label label--wide" style="left:861px; top:1655px;">
    <div class="brand-tab">HALLBRUNNER</div>
    <div class="house-line">EDELBRÄNDE</div>
    <div class="variety"><div class="origin">TÜRKEN</div><div class="script-name">Kirsche</div></div>
    <div class="product"><span class="ornament" role="img" aria-label="Rotes Zierornament"></span><span class="product-text">BRAND</span><span class="ornament" role="img" aria-label="Rotes Zierornament"></span></div>
    <div class="maker"><span class="maker-dot"></span>Hallbrunner</div>
    <div class="address"><p>Edeldestillerie Hallbrunner · Lindenhofweg 4 · 79110 Sonnbach</p><p class="web">www.<span>brennerei-hallbrunner</span>.de</p><p>Losnummer K3F57382</p></div>
    <div class="specs"><span>40 % VOL.</span><span>500 ML ℮</span></div>
  </article>
</main>
</body>
</html>
```